Doctor Formulated Medical Cosmetics

Halvessa Rue is an E-commerce site for high end Medical Cosmetics designed to treat specific skin problems. The Halvessa Rue difference/advantage is that all creams and serums are:
Doctor Formulated, Freshly Handmade, Registered Pharmacy.
The Site also provides real doctor Dermatology Consultations, Library (with a list of - 1. Active Ingredients in the creams with description of their effects, 2. Skin Conditions with information on what causes the condition and typical treatment approaches and outcomes. 3. Resources from Dermatology Journals and literature on the conditions.)
Header Information: Halvessa Rue, languages EN, BG, Register / log in, Shopping Bag. This field should be narrow.
Categories (horizontal): Home, Face, Body, Hair Care, Skin Conditions, Doctor Consultation, Library
The Landing Page should have only one well organized picture, which is intended to create the feeling of luxury, freedom and relaxation. It will be large and will fill the whole screen. All text should be on transparent or similar color fields. Please use the color of the text to create also the feeling of conservative luxury.
Written message / image overlay Halvessa Rue(logo), Skin Care, Doctor Formulated, Freshly Handmade, Registered Pharmacy.
Please study the Landing Page of this site as an example: www.marivelta.com
Under the Landing Page, there should be a slider with 4 of our products.
Underneath: Four Blog Articles (large pictures for maximum impact and luxury text underneath).
Underneath: Banner for Dermatologist Consultation, (button for Start Your Case Now).
Underneath: Two pictures in a line - Library (with books), and Active Ingredients.
Footer: Philosophy, Categories, Customer Care
Please adhere to the color palate provided in the pictures (as attachments). Provided are some examples of Web Sites with the desired look and feel. www.quillon.com , www.tavishrowe.com .
Please use different shades of gray, white, beige and gold colors, and black. Our products will be in brown glass jars and bottles to convey the professional, pharmacy made nature of the creams and lotions.
We find the following Front Page very attractive and effective - www.marivelta.com , with its full page image and overlaying text.
Please have a look at this link for the Landing page.
http://www.framstockly.com/detail/video/woman-lying-on-a-black-sand-beach-in-a-bikini-stock-footage/31862074
I would like to use it in the animated version to achieve the WOW effect. I have uploaded the jpeg version for it, so you will be able create your design.
For the Landing page design, please use only the two uploaded pictures of a woman laying at the beach. Let's see how each of them will look like.
Thank you for your help.

```html
<!DOCTYPE html>
<html lang="en">
<head>
<meta charset="utf-8">
<title>Halvessa Rue — Doctor Formulated Medical Cosmetics</title>
<link href="https://fonts.googleapis.com/css2?family=Playfair+Display:wght@400;700&family=Lato:wght@400;700&display=swap" rel="stylesheet">
<style>
:root{
  --black:#111111;
  --ink:#2b2b2b;
  --muted:#6d6a66;
  --gold:#c7a15a;
  --gold-dark:#a98440;
  --brown:#3a2a1f;
  --beige:#ebe5dc;
  --paper:#f6f3ee;
  --gray:#e8e8ea;
  --white:#ffffff;
  --serif:"Playfair Display", Georgia, serif;
  --sans:"Lato", Arial, sans-serif;
}
*{box-sizing:border-box;margin:0;padding:0}
html,body{width:1200px;height:2164px;overflow:hidden}
body{font-family:var(--sans);color:var(--ink);background:var(--white);position:relative}
a{color:inherit;text-decoration:none}

.topbar{height:32px;background:var(--black);color:#cfcfcf;font-size:11px;display:flex;align-items:center;justify-content:flex-end;gap:26px;padding:0 150px}
.topbar .cart{color:var(--gold)}

.mainnav{height:100px;display:flex;align-items:center;justify-content:space-between;padding:0 150px;background:var(--white)}
.brand{display:flex;align-items:center;gap:10px;font-family:var(--serif);font-size:26px;color:var(--gold-dark)}
.brand .dot{width:22px;height:22px;border-radius:50%;border:2px solid var(--gold)}
.menu{display:flex;gap:6px;font-size:12px}
.menu a{padding:7px 12px;color:var(--ink)}
.menu a.active{background:var(--gold);color:var(--white)}

.hero{position:relative;height:428px;background:linear-gradient(100deg,#e7ddd0 0%,#cdb59b 35%,#9c8773 70%,#d8ccbd 100%)}
.hero-copy{position:absolute;left:0;right:0;top:140px;text-align:center;color:var(--white)}
.hero-copy h1{font-family:var(--serif);font-weight:400;font-size:32px;line-height:1.25;text-shadow:0 1px 3px rgba(0,0,0,.25)}
.btn{display:inline-block;font-size:11px;padding:9px 18px;letter-spacing:.5px}
.btn-outline{border:1px solid var(--white);color:var(--white);margin-top:22px;background:rgba(0,0,0,.15)}
.btn-gold{background:var(--gold);color:var(--white)}
.btn-dark{background:var(--brown);color:var(--white);padding:6px 14px;font-size:10px}

.slider{display:grid;grid-template-columns:repeat(4,1fr);height:200px}
.tile{position:relative;background:linear-gradient(135deg,#c9c6c1,#8f8a84);border-right:2px solid var(--white);overflow:hidden}
.tile .pack{position:absolute;right:30px;top:34px;width:96px;height:130px;background:linear-gradient(180deg,#5b3a22,#2b1a10);border-radius:8px}
.tile.bottle .pack{width:56px;right:50px;border-radius:6px 6px 10px 10px}
.tile h3{position:absolute;left:16px;top:40px;font-family:var(--serif);font-size:21px;color:var(--white);font-weight:700}
.tile .btn-dark{position:absolute;left:16px;top:118px}

.section{padding:0 150px}
.row{display:flex;gap:40px}
.heading{font-family:var(--serif);font-size:22px;color:var(--ink);font-weight:700}
.blog-area{margin-top:68px}
.blog{width:500px}
.cards{display:flex;gap:28px;margin-top:22px}
.card{width:224px;height:400px;background:var(--beige)}
.card .photo{height:170px;background:linear-gradient(160deg,#b08b6e,#4a3326)}
.card .photo.alt{background:linear-gradient(200deg,#c4a487,#5a3f30)}
.card .tag{display:block;width:44px;height:44px;background:var(--gold);margin:-22px 0 0 18px;position:relative}
.card p{font-size:12px;line-height:1.5;color:var(--muted);padding:14px 18px 0}
.card .more{font-size:11px;color:var(--ink);padding:16px 18px;display:block}
.consult{width:460px}
.consult-box{margin-top:22px;height:400px;background:linear-gradient(180deg,#4a3628,#2f2119);padding:36px 26px;color:#d9cfc4}
.consult-box h2{font-family:var(--serif);font-weight:400;font-size:28px;color:var(--white);line-height:1.25}
.consult-box p{font-size:12px;line-height:1.6;margin:20px 0 26px;width:250px}

.banner{margin:52px 150px 0;height:160px;background:var(--beige);position:relative}
.banner h2{position:absolute;left:34px;top:24px;font-family:var(--serif);font-size:30px;line-height:1.15;font-weight:400;color:var(--ink)}
.banner p{position:absolute;left:34px;top:96px;width:440px;font-size:11px;line-height:1.5;color:var(--muted)}
.banner .bottle{position:absolute;right:150px;top:14px;width:70px;height:132px;background:linear-gradient(180deg,#262626,#0d0d0d);border-radius:6px}

.products-area{margin-top:52px}
.products{display:grid;grid-template-columns:repeat(4,1fr);margin-top:30px;text-align:center}
.product .shot{height:120px;width:140px;margin:0 auto;background:linear-gradient(180deg,#e8e4de,#cfc8bf)}
.product h4{font-size:11px;font-weight:400;margin-top:14px;color:var(--ink)}
.stars{display:flex;justify-content:center;gap:3px;margin-top:8px}

.footer{position:absolute;left:0;right:0;top:1864px;height:264px;background:var(--gray);padding:46px 150px 0;display:grid;grid-template-columns:repeat(3,1fr);gap:40px}
.footer h5{font-family:var(--serif);font-size:22px;font-weight:400;color:var(--ink)}
.footer p{font-size:11px;line-height:1.6;color:var(--muted);margin-top:16px}
.footer a{display:block;font-size:11px;font-weight:700;margin-top:16px}
.copyright{position:absolute;left:0;right:0;bottom:0;height:36px;background:var(--black);color:#bcbcbc;font-size:10px;display:flex;align-items:center;justify-content:center}
</style>
</head>
<body>

<header>
  <div class="topbar">
    <span>info@halvessarue.com</span><span>Language: EN · BG</span><span>My Account</span><span>Register / Log in</span><span class="cart">Shopping Bag (0)</span>
  </div>
  <nav class="mainnav">
    <a class="brand" href="#"><span class="dot"></span>Halvessa Rue</a>
    <div class="menu">
      <a class="active" href="#">Home</a><a href="#">Face</a><a href="#">Body</a><a href="#">Hair Care</a><a href="#">Skin Conditions</a><a href="#">Dermatologist Consultation</a><a href="#">Library</a>
    </div>
  </nav>
</header>

<section class="hero" role="img" aria-label="Woman relaxing on a beach, warm light">
  <div class="hero-copy">
    <h1>Doctor Formulated, Freshly Handmade,<br>Registered Pharmacy, Highest Ethical Standards.</h1>
    <a class="btn btn-outline" href="#">Explore More</a>
  </div>
</section>

<section class="slider">
  <div class="tile"><div class="pack" role="img" aria-label="Brown glass jar of balancing gel"></div><h3>Balancing Gel</h3><a class="btn btn-dark" href="#">Shop Now</a></div>
  <div class="tile"><div class="pack" role="img" aria-label="Brown glass jar of moisture cream"></div><h3>Immediate Moisture</h3><a class="btn btn-dark" href="#">Shop Now</a></div>
  <div class="tile bottle"><div class="pack" role="img" aria-label="Dropper bottle of eye lid serum"></div><h3>Eye Lid Serum</h3><a class="btn btn-dark" href="#">Shop Now</a></div>
  <div class="tile bottle"><div class="pack" role="img" aria-label="Dropper bottle of moisture serum"></div><h3>Immediate Moisture</h3><a class="btn btn-dark" href="#">Shop Now</a></div>
</section>

<section class="section blog-area">
  <div class="row">
    <div class="blog">
      <h2 class="heading">Our Blog</h2>
      <div class="cards">
        <article class="card">
          <div class="photo" role="img" aria-label="Portrait photo for skin care article"></div>
          <span class="tag"></span>
          <p>Gentle care is key to healthy skin, every day.</p>
          <p>Simple routines with pure ingredients bring calm, balance and a lasting natural glow.</p>
          <a class="more" href="#">Read more ›</a>
        </article>
        <article class="card">
          <div class="photo alt" role="img" aria-label="Portrait photo for beauty article"></div>
          <span class="tag"></span>
          <p>Gentle care is key to healthy skin, every day.</p>
          <p>Simple routines with pure ingredients bring calm, balance and a lasting natural glow.</p>
          <a class="more" href="#">Read more ›</a>
        </article>
      </div>
    </div>
    <div class="consult">
      <h2 class="heading">Dermatologist Consultation</h2>
      <div class="consult-box" role="img" aria-label="Woman with flowing hair in soft dark tones">
        <h2>Beauty Sleep<br>With Real Result</h2>
        <p>Our doctors review your skin history, concerns and daily habits, then suggest a tailored routine. Share photos and notes in a private case, and receive clear guidance on treatment, expected outcomes and the freshly made products best suited to your skin.</p>
        <a class="btn btn-gold" href="#">Start Your Case Now</a>
      </div>
    </div>
  </div>
</section>

<section class="banner">
  <h2>Acyl-Glutathione<br>Eye Lid Serum</h2>
  <p>Formulated with care to lift and firm the delicate eye area. Active ingredients help reduce fine lines, visible puffiness and dark circles, leaving skin smooth, bright and refreshed morning after morning.</p>
  <div class="bottle" role="img" aria-label="Dark dropper bottle of eye lid serum"></div>
</section>

<section class="section products-area">
  <h2 class="heading">Our Product</h2>
  <div class="products">
    <div class="product"><div class="shot" role="img" aria-label="Jar of balancing gel"></div><h4>Tea Oil Balancing Gel</h4><div class="stars"><svg width="60" height="10"><g fill="#2b2b2b"><circle cx="5" cy="5" r="3.5"/><circle cx="17" cy="5" r="3.5"/><circle cx="29" cy="5" r="3.5"/><circle cx="41" cy="5" r="3.5"/><circle cx="53" cy="5" r="3.5"/></g></svg></div></div>
    <div class="product"><div class="shot" role="img" aria-label="Bottle of moisture serum"></div><h4>Immediate Moisture</h4><div class="stars"><svg width="60" height="10"><g fill="#2b2b2b"><circle cx="5" cy="5" r="3.5"/><circle cx="17" cy="5" r="3.5"/><circle cx="29" cy="5" r="3.5"/><circle cx="41" cy="5" r="3.5"/><circle cx="53" cy="5" r="3.5"/></g></svg></div></div>
    <div class="product"><div class="shot" role="img" aria-label="Bottle of eye lid serum"></div><h4>Acyl-Glutathione Eye Lid Serum</h4><div class="stars"><svg width="60" height="10"><g fill="#2b2b2b"><circle cx="5" cy="5" r="3.5"/><circle cx="17" cy="5" r="3.5"/><circle cx="29" cy="5" r="3.5"/><circle cx="41" cy="5" r="3.5"/><circle cx="53" cy="5" r="3.5"/></g></svg></div></div>
    <div class="product"><div class="shot" role="img" aria-label="Bottle of oxidant serum"></div><h4>Anti-Oxidant Duo Serum</h4><div class="stars"><svg width="60" height="10"><g fill="#2b2b2b"><circle cx="5" cy="5" r="3.5"/><circle cx="17" cy="5" r="3.5"/><circle cx="29" cy="5" r="3.5"/><circle cx="41" cy="5" r="3.5"/><circle cx="53" cy="5" r="3.5"/></g></svg></div></div>
  </div>
</section>

<footer class="footer">
  <div>
    <h5>Philosophy</h5>
    <p>Every cream and serum is doctor formulated and made fresh by hand in our registered pharmacy, with honest ingredients and the highest ethical standards.</p>
    <a href="#">Read More</a>
  </div>
  <div>
    <h5>Our Doctors</h5>
    <p>Experienced dermatologists guide each formula and personal consultation.<br>Skin Conditions<br>Active Ingredients<br>Resources</p>
    <a href="#">Read More</a>
  </div>
  <div>
    <h5>Customer Care</h5>
    <p>Contact Us<br>Shipping Information<br>Returns and Exchanges<br>Order Status<br>Consultation Access<br>FAQ</p>
  </div>
</footer>
<div class="copyright">2016 © Halvessa Rue</div>

</body>
</html>
```